Business Card Design Project

Require a business card for a swing band called "Velvet Brass Parade". We are a 6 piece band that performs at events and corporate functions. Our music is great for dancing to or just providing a classy background atmosphere for people to enjoy. Final design should communicate professionalism and style with a hint of fun.

Sorry, just realised that it needs to be single sided only. Also, no rounded edges.

Industry/Entity Type

Events

Requirements
Must have
• Contact number: 0438 216 903
email address: velvetbrassparade@mailbox-demo.net
Website details: www.velvetbrassparade-demo.com

```html
<!DOCTYPE html>
<html lang="en">
<head>
<meta charset="utf-8">
<title>Velvet Brass Parade – Business Card</title>
<link rel="stylesheet" href="https://fonts.googleapis.com/css2?family=Dancing+Script:wght@500&family=Source+Sans+3:wght@400&display=swap">
<style>
  :root {
    --page: #ffffff;
    --card-top: #fbfaf4;
    --card-bottom: #e4e0cc;
    --band-start: #f7d672;
    --band-end: #ea8a2e;
    --sheet: #ffffff;
    --title: #ef8a1f;
    --ink: #1c1c1c;
    --search-blue: #1f73b8;
    --input: #ffffff;
    --input-edge: #9aa6b0;
  }
  html, body {
    margin: 0;
    padding: 0;
    width: 1200px;
    height: 721px;
    overflow: hidden;
    background: var(--page);
  }
  .card-canvas { display: block; width: 1200px; height: 721px; }
  .band-title {
    font-family: "Dancing Script", cursive;
    font-size: 76px;
    fill: var(--title);
  }
  .contact-line {
    font-family: "Source Sans 3", sans-serif;
    font-size: 31px;
    fill: var(--ink);
  }
  .web-address {
    font-family: "Source Sans 3", sans-serif;
    font-size: 29px;
    fill: var(--ink);
  }
</style>
</head>
<body>
<svg class="card-canvas" viewBox="0 0 1200 721" xmlns="http://www.w3.org/2000/svg">
  <defs>
    <linearGradient id="card-fill" x1="0" y1="0" x2="0" y2="1">
      <stop offset="0" stop-color="var(--card-top)"/>
      <stop offset="1" stop-color="var(--card-bottom)"/>
    </linearGradient>
    <linearGradient id="band-fill" x1="0" y1="0" x2="1" y2="0">
      <stop offset="0" stop-color="var(--band-start)"/>
      <stop offset="1" stop-color="var(--band-end)"/>
    </linearGradient>
    <radialGradient id="party-fill" cx="0.5" cy="0.65" r="0.6">
      <stop offset="0" stop-color="#e9c85a"/>
      <stop offset="0.45" stop-color="#9fc7d6"/>
      <stop offset="0.8" stop-color="#d8d3c2"/>
      <stop offset="1" stop-color="#e4e0cc" stop-opacity="0"/>
    </radialGradient>
    <clipPath id="card-clip">
      <rect x="38" y="38" width="1119" height="640"/>
    </clipPath>
    <filter id="sheet-shadow" x="-10%" y="-10%" width="130%" height="130%">
      <feDropShadow dx="2" dy="4" stdDeviation="5" flood-color="#000" flood-opacity="0.18"/>
    </filter>
  </defs>

  <g class="business-card" clip-path="url(#card-clip)">
    <rect class="card-face" x="38" y="38" width="1119" height="640" fill="url(#card-fill)"/>

    <text class="band-title" transform="translate(88 282) rotate(-12.5)">Velvet Brass Parade</text>

    <g class="contact-band" transform="translate(315 288) rotate(-12.5)">
      <rect class="band-sheet" x="-22" y="22" width="1000" height="300" fill="var(--sheet)" filter="url(#sheet-shadow)" transform="rotate(2.5)"/>
      <rect class="band-strip" x="0" y="0" width="1000" height="300" fill="url(#band-fill)"/>

      <text class="contact-line" x="100" y="98">Phone: 0438 216 903</text>
      <text class="contact-line" x="115" y="158">email: velvetbrassparade@mailbox-demo.net</text>

      <g class="web-search">
        <rect class="search-frame" x="125" y="190" width="620" height="92" rx="14" fill="var(--search-blue)"/>
        <rect class="search-input" x="140" y="206" width="500" height="60" rx="10" fill="var(--input)" stroke="var(--input-edge)" stroke-width="3"/>
        <text class="web-address" x="156" y="246">www.velvetbrassparade-demo.com</text>
        <g class="search-icon" fill="none" stroke="var(--input)" stroke-width="6" stroke-linecap="round">
          <circle cx="697" cy="229" r="15"/>
          <line x1="686" y1="241" x2="671" y2="257"/>
        </g>
      </g>
    </g>

    <g class="party-illustration" role="img" aria-label="Illustration of colourful eggs with rising bubbles">
      <rect x="820" y="455" width="300" height="200" rx="100" fill="url(#party-fill)"/>
    </g>
  </g>
</svg>
</body>
</html>
```